Boutique Wealth management firm needs a new business card design

I want to update my business card design to be more consistent with the look and feel of my website (www.brisvane-wealth.com). I would like to incorporate an ivory parchment background and am open to switching from the current "portrait" layout to a more traditional "landscape" orientation. The final design should convey stability and exclusivity and I want something in PDF format that is ready to send to the printer

Thank you all for taking the time to submit your designs for my project. I've made my decision and picked the design I like best. Thanks again!

```html
<!DOCTYPE html>
<html lang="en">
<head>
<meta charset="utf-8">
<title>Brisvane Wealth Advisory – Business Card</title>
<link rel="stylesheet" href="https://fonts.googleapis.com/css2?family=Libre+Baskerville:wght@400;700&family=Tinos:wght@400;700&display=swap">
<style>
  :root {
    --page: #ffffff;
    --olive: #635829;
    --maroon: #7a2233;
    --ink: #1e1a16;
    --parchment-light: #fbefc8;
    --parchment-mid: #f6e2a8;
    --parchment-deep: #f1d796;
  }
  html, body {
    margin: 0;
    padding: 0;
    width: 1200px;
    height: 829px;
    overflow: hidden;
    background: var(--page);
  }
  .canvas {
    position: relative;
    width: 1200px;
    height: 829px;
  }
  .card {
    position: absolute;
    left: 216px;
    top: 208px;
    width: 810px;
    height: 463px;
    overflow: hidden;
    font-family: "Tinos", "Times New Roman", serif;
    color: var(--ink);
  }
  .parchment {
    position: absolute;
    inset: 0;
    background:
      radial-gradient(ellipse at 30% 40%, var(--parchment-light) 0%, transparent 60%),
      radial-gradient(ellipse at 80% 70%, var(--parchment-light) 0%, transparent 55%),
      linear-gradient(135deg, var(--parchment-mid), var(--parchment-deep) 50%, var(--parchment-mid));
  }
  .band-top {
    position: absolute;
    left: 0; top: 0;
    width: 100%;
    height: 20px;
    background: var(--olive);
  }
  .rule-top {
    position: absolute;
    left: 0; top: 20px;
    width: 100%;
    height: 6px;
    background: var(--maroon);
  }
  .band-bottom {
    position: absolute;
    left: 0; bottom: 0;
    width: 100%;
    height: 9px;
    background: var(--maroon);
  }
  .brand {
    position: absolute;
    left: 32px;
    top: 60px;
    margin: 0;
    font-family: "Libre Baskerville", "Georgia", serif;
    font-weight: 700;
    color: var(--maroon);
    line-height: 1;
  }
  .brand-name {
    display: block;
    font-size: 46px;
    letter-spacing: 3px;
  }
  .brand-sub {
    display: block;
    font-size: 27px;
    margin: 6px 0 0 82px;
  }
  .tagline {
    position: absolute;
    left: 32px;
    top: 202px;
    margin: 0;
    font-size: 22px;
    line-height: 32px;
  }
  .tagline .accent {
    color: var(--maroon);
    font-size: 28px;
  }
  .contact {
    position: absolute;
    left: 32px;
    top: 336px;
    margin: 0;
    font-size: 22px;
    line-height: 26px;
    font-style: normal;
  }
  .license {
    position: absolute;
    left: 32px;
    top: 427px;
    margin: 0;
    font-size: 16px;
    font-weight: 700;
  }
  .person {
    position: absolute;
    left: 464px;
    top: 200px;
    margin: 0;
    font-family: "Libre Baskerville", "Georgia", serif;
    font-weight: 700;
    font-size: 31px;
    line-height: 39px;
    color: var(--maroon);
    white-space: nowrap;
  }
  .mailing {
    position: absolute;
    left: 526px;
    top: 338px;
    margin: 0;
    font-size: 23px;
    line-height: 29px;
    font-style: normal;
  }
</style>
</head>
<body>
<div class="canvas">
  <div class="card">
    <div class="parchment" role="img" aria-label="Ivory parchment paper texture"></div>
    <div class="band-top"></div>
    <div class="rule-top"></div>

    <h1 class="brand">
      <span class="brand-name">BRISVANE</span>
      <span class="brand-sub">Wealth Advisory</span>
    </h1>

    <p class="tagline">Shaping your<br><span class="accent">plans</span> and <span class="accent">legacy</span></p>

    <address class="contact">
      925-555-0184<br>
      dale@brisvane-wealth.com<br>
      www.brisvane-wealth.com
    </address>

    <p class="license">CA Insurance License #0K57218</p>

    <p class="person">Dale Wren, MBA<br>Principal</p>

    <address class="mailing">
      Mailing Address:<br>
      2318 N. Alder Rd. #214<br>
      Pleasanton, CA 94566
    </address>

    <div class="band-bottom"></div>
  </div>
</div>
</body>
</html>
```